Business Card Design Project

Corwen Property Management

Our Business is residential property management, we therefore need a card that displays a professional image, but is clear and concise, and easy to read
Updates

We are committed now guys and girls, loving what we are seeing so far! 

Target Market(s)

Landlords, Rental Property Owners

Industry/Entity Type

Residential

Requirements
Must have
• Dean Fosterly - Principal
Tessa Fosterly - Director (Property Management)

PO Box 718
Holloway SA 5093

Dean: 0419 372 508
Tessa: 0419 613 947

www.corwenpropertymanagement.com.au
admin@corwenpropertymanagement.com.au

Nice to have
• I would like the card to be double sided, white background on the information side and then colour on the reverse, in blue or black and incorporating our logo

```html
<!DOCTYPE html>
<html lang="en">
<head>
<meta charset="utf-8">
<title>Corwen Property Management – Business Card</title>
<link rel="stylesheet" href="https://fonts.googleapis.com/css2?family=Arimo:wght@400;700&display=swap">
<style>
  :root {
    --page: #e6e6e4;
    --card-white: #ffffff;
    --card-dark: #2a2524;
    --brand-blue: #1f6fb4;
    --ink: #333333;
    --ink-soft: #555555;
    --on-dark: #f2f2f2;
    --on-dark-soft: #d8d8d8;
  }
  * { box-sizing: border-box; margin: 0; padding: 0; }
  html, body { width: 1200px; height: 951px; overflow: hidden; }
  body {
    background: var(--page);
    font-family: "Arimo", Arial, sans-serif;
    position: relative;
  }
  .card {
    position: absolute;
    width: 620px;
    height: 378px;
    border-radius: 22px;
    overflow: hidden;
    box-shadow: 0 8px 22px rgba(0,0,0,0.22);
  }
  /* Front */
  .card--front { left: 90px; top: 70px; background: var(--card-white); }
  .brand {
    position: absolute;
    display: flex;
    align-items: center;
    gap: 14px;
  }
  .brand__mark { width: 46px; height: 46px; background: var(--brand-blue); flex: none; }
  .brand__name { font-weight: 700; line-height: 1.05; }
  .card--front .brand { left: 120px; top: 120px; }
  .card--front .brand__name { font-size: 34px; color: var(--ink); }
  .card--front .website {
    position: absolute; left: 0; right: 0; top: 248px;
    text-align: center; font-size: 17px; color: var(--ink);
  }
  /* Back */
  .card--back { left: 490px; top: 500px; background: var(--card-dark); }
  .card__swoosh { position: absolute; inset: 0; }
  .people {
    position: absolute; left: 72px; top: 62px; width: 170px;
    text-align: center; color: var(--on-dark);
  }
  .person__name { font-size: 18px; }
  .person__role { font-size: 14px; color: var(--on-dark-soft); margin-bottom: 6px; }
  .divider {
    position: absolute; left: 262px; top: 62px; width: 1px; height: 120px;
    background: var(--on-dark-soft);
  }
  .contacts {
    position: absolute; left: 278px; top: 60px; list-style: none;
    color: var(--on-dark); font-size: 15px;
  }
  .contacts li { display: flex; align-items: flex-start; gap: 10px; line-height: 20px; }
  .contacts li.address { margin-bottom: 10px; }
  .contacts svg { flex: none; margin-top: 3px; }
  .card--back .brand { left: 40px; top: 264px; }
  .card--back .brand__mark { width: 40px; height: 40px; }
  .card--back .brand__name { font-size: 26px; color: var(--on-dark); }
</style>
</head>
<body>

<section class="card card--front">
  <div class="brand">
    <span class="brand__mark"></span>
    <span class="brand__name">Corwen<br>Property Management</span>
  </div>
  <p class="website">www.corwenpropertymanagement.com.au</p>
</section>

<section class="card card--back">
  <svg class="card__swoosh" width="620" height="378" viewBox="0 0 620 378" aria-hidden="true">
    <path d="M0 0 H110 Q40 25 0 120 Z" fill="var(--brand-blue)"/>
    <path d="M0 140 Q40 28 150 0" fill="none" stroke="#ffffff" stroke-width="4"/>
    <path d="M620 378 H470 Q585 345 620 220 Z" fill="var(--brand-blue)"/>
    <path d="M420 378 Q590 350 620 190" fill="none" stroke="#ffffff" stroke-width="6"/>
  </svg>

  <div class="people">
    <p class="person__name">Dean Fosterly</p>
    <p class="person__role">Principal</p>
    <p class="person__name">Tessa Fosterly</p>
    <p class="person__role">Director<br>(Property Management)</p>
  </div>

  <div class="divider"></div>

  <ul class="contacts">
    <li class="address">
      <svg width="14" height="14" viewBox="0 0 14 14"><path d="M7 1 L13 7 H11 V13 H3 V7 H1 Z" fill="#fff"/></svg>
      <span>PO Box 718<br>Holloway SA 5093</span>
    </li>
    <li>
      <svg width="14" height="14" viewBox="0 0 14 14"><circle cx="7" cy="7" r="6.5" fill="#fff"/><path d="M4.5 3.5 L6 3.5 L6.5 5.5 L5.5 6.2 Q6.5 8 7.8 8.5 L8.5 7.5 L10.5 8 L10.5 9.5 Q6 10 4.5 3.5 Z" fill="var(--card-dark)"/></svg>
      <span>Dean: 0419 372 508</span>
    </li>
    <li>
      <svg width="14" height="14" viewBox="0 0 14 14"><circle cx="7" cy="7" r="6.5" fill="#fff"/><path d="M4.5 3.5 L6 3.5 L6.5 5.5 L5.5 6.2 Q6.5 8 7.8 8.5 L8.5 7.5 L10.5 8 L10.5 9.5 Q6 10 4.5 3.5 Z" fill="var(--card-dark)"/></svg>
      <span>Tessa: 0419 613 947</span>
    </li>
    <li>
      <svg width="14" height="14" viewBox="0 0 14 14"><circle cx="7" cy="7" r="6.5" fill="#fff"/><path d="M1 7 H13 M7 1 Q3 7 7 13 M7 1 Q11 7 7 13" fill="none" stroke="var(--card-dark)" stroke-width="1"/></svg>
      <span>www.corwenpropertymanagement.com.au</span>
    </li>
    <li>
      <svg width="14" height="14" viewBox="0 0 14 14"><circle cx="7" cy="7" r="6.5" fill="#fff"/><rect x="3.5" y="4.5" width="7" height="5" fill="none" stroke="var(--card-dark)" stroke-width="1"/><path d="M3.5 4.5 L7 7.5 L10.5 4.5" fill="none" stroke="var(--card-dark)" stroke-width="1"/></svg>
      <span>admin@corwenpropertymanagement.com.au</span>
    </li>
  </ul>

  <div class="brand">
    <span class="brand__mark"></span>
    <span class="brand__name">Corwen<br>Property Management</span>
  </div>
</section>

</body>
</html>
```